TRIVAN 2026 Flyer for Conference

TRIVAN needs a design for a 1-page flyer that we will hand out at an upcoming event & then later post online as a pdf. There are 3 elements which need to be on the flyer:

1) A logo. This should be prominent on the design (e.g., in the middle). The flyer should use the colors that are in that logo (e.g., for accents, design elements, and/or text; not all of these have to be used):
Dark blue: #185577
Med blue: #327C9A
Teal: #4EB1C2
Light Teal: #9EDBE6

2) The conference theme -- Forests of Wonder: Climbing toward Research Fluency -- should be at the flyer's top.

3) Finally, these six tracks should be listed below the theme and the logo (it's font size should be at least a couple sizes smaller than the size used for the theme):
- Pearls of Pedagogy: Teaching Techniques that Work
- The Depth Gauge: Measuring Instructional Impact
- Techtonic Shifts: Innovation and Educational Technology
- Captain's Log: Navigating Leadership in Library Instruction
- Swimming Together: Collaborating with Others
- The Bermuda Triangle: Exploring (Seemingly) Eternal Challenges

Font styles to use
Sans Serif

Colors
0094D4
00A9DD
6FCCEA
C7EBF8
E9F6FB

Requirements
Must have
• The 3 elements listed in the description: 1) the logo, 2) the text of the theme and 3) the text for the tracks.

```html
<!DOCTYPE html>
<html lang="en">
<head>
<meta charset="utf-8">
<title>TRIVAN 2026 – Forests of Wonder</title>
<link href="https://fonts.googleapis.com/css2?family=Bebas+Neue&family=Montserrat:wght@500;600;700;800&display=swap" rel="stylesheet">
<style>
  :root {
    --dark-blue: #185577;
    --band-blue: #1d5a7c;
    --med-blue: #327C9A;
    --teal: #4EB1C2;
    --light-teal: #9EDBE6;
    --pale: #E9F6FB;
    --number-grey: #4a5561;
    --text-dark: #1f2a33;
    --white: #ffffff;
  }
  * { margin: 0; padding: 0; box-sizing: border-box; }
  html, body { width: 891px; height: 1200px; overflow: hidden; background: var(--white); }
  .flyer {
    position: relative; width: 891px; height: 1200px; overflow: hidden;
    background: var(--white);
    font-family: "Montserrat", sans-serif;
  }
  .pattern-top {
    position: absolute; left: 0; top: 0; width: 891px; height: 420px;
    background:
      radial-gradient(ellipse 300px 260px at 0 0, rgba(158,219,230,.75), transparent 70%),
      radial-gradient(ellipse 300px 260px at 891px 0, rgba(158,219,230,.75), transparent 70%),
      radial-gradient(ellipse 500px 120px at 50% 0, rgba(158,219,230,.35), transparent 80%);
  }
  .brand {
    position: absolute; top: 92px; left: 0; width: 100%;
    display: flex; justify-content: center; align-items: center; gap: 12px;
  }
  .brand-dot { width: 34px; height: 34px; border-radius: 50%; background: var(--teal); }
  .brand-name { font-weight: 800; font-size: 38px; color: var(--dark-blue); letter-spacing: 1px; }
  .theme { position: absolute; top: 198px; left: 0; width: 100%; text-align: center; }
  .theme-title {
    font-weight: 700; font-size: 62px; line-height: 62px; color: var(--dark-blue);
    letter-spacing: 1px; text-transform: uppercase;
  }
  .theme-sub {
    margin-top: 12px; font-weight: 600; font-size: 30px; line-height: 36px;
    color: var(--teal); text-transform: uppercase;
  }
  .track { position: absolute; width: 366px; height: 108px; }
  .track-shadow {
    position: absolute; left: 44px; top: 10px; width: 300px; height: 98px;
    background: #d6d9dc; border-radius: 8px;
  }
  .track-tab {
    position: absolute; left: 346px; top: 12px; width: 18px; height: 80px;
    background: var(--teal); border-radius: 0 5px 5px 0;
  }
  .track-card {
    position: absolute; left: 40px; top: 0; width: 310px; height: 100px;
    background: linear-gradient(90deg, #e4f1f8, var(--white) 70%);
    border: 3px solid #cfeaf2; border-radius: 8px;
  }
  .track-ring {
    position: absolute; left: 0; top: -3px; width: 106px; height: 106px; border-radius: 50%;
    background: var(--white);
    border: 8px solid var(--teal);
    border-bottom-color: var(--med-blue); border-left-color: var(--med-blue);
    display: flex; align-items: center; justify-content: center;
    font-family: "Bebas Neue", sans-serif; font-size: 50px; color: var(--number-grey);
  }
  .track-text { position: absolute; left: 130px; top: 22px; width: 208px; }
  .track-name {
    font-family: "Bebas Neue", sans-serif; font-weight: 400; font-size: 24px; line-height: 24px;
    color: var(--med-blue); letter-spacing: .2px; white-space: nowrap;
  }
  .track-desc { margin-top: 5px; font-weight: 500; font-size: 11.5px; line-height: 13px; color: var(--text-dark); }
  .books {
    position: absolute; left: 305px; top: 855px; width: 280px; height: 133px;
    background: linear-gradient(90deg, #8a6a55, #c9c2b4 30%, #b4323a 50%, #e8dcc0 75%, #c79a5a);
    border-radius: 3px; z-index: 2;
  }
  .footer-band { position: absolute; left: 0; top: 860px; width: 891px; height: 340px; }
  .footer-text { position: absolute; left: 0; top: 1014px; width: 100%; text-align: center; }
  .footer-title { font-family: "Bebas Neue", sans-serif; font-size: 68px; line-height: 66px; color: var(--white); letter-spacing: 1px; }
  .footer-meta { margin-top: 4px; font-weight: 700; font-size: 25px; line-height: 30px; color: var(--teal); }
  .web-pill {
    position: absolute; left: 338px; top: 1137px; width: 216px; height: 26px;
    background: var(--teal); border-radius: 13px;
    display: flex; align-items: center; gap: 8px; padding-left: 6px;
    font-weight: 500; font-size: 13px; color: var(--white);
  }
  .web-icon { width: 18px; height: 18px; }
</style>
</head>
<body>
<main class="flyer">
  <div class="pattern-top" role="img" aria-label="Soft halftone dot pattern in light teal"></div>

  <header class="brand">
    <span class="brand-dot"></span>
    <span class="brand-name">TRIVAN 2026</span>
  </header>

  <section class="theme">
    <h1 class="theme-title">Forests of<br>Wonder</h1>
    <p class="theme-sub">Climbing toward Research<br>Fluency</p>
  </section>

  <section class="tracks">
    <div class="track" style="left:69px;top:449px">
      <div class="track-shadow"></div><div class="track-tab"></div><div class="track-card"></div>
      <div class="track-ring">1</div>
      <div class="track-text"><h2 class="track-name">Pearls of Pedagogy</h2><p class="track-desc">Teaching Techniques<br>that Work</p></div>
    </div>
    <div class="track" style="left:455px;top:449px">
      <div class="track-shadow"></div><div class="track-tab"></div><div class="track-card"></div>
      <div class="track-ring">2</div>
      <div class="track-text"><h2 class="track-name">The Depth Gauge</h2><p class="track-desc">Measuring Instructional<br>Impact</p></div>
    </div>
    <div class="track" style="left:69px;top:586px">
      <div class="track-shadow"></div><div class="track-tab"></div><div class="track-card"></div>
      <div class="track-ring">3</div>
      <div class="track-text"><h2 class="track-name">Techtonic Shifts</h2><p class="track-desc">Innovation and<br>Educational Technology</p></div>
    </div>
    <div class="track" style="left:455px;top:586px">
      <div class="track-shadow"></div><div class="track-tab"></div><div class="track-card"></div>
      <div class="track-ring">4</div>
      <div class="track-text"><h2 class="track-name">Captain's Log</h2><p class="track-desc">Navigating Leadership<br>in Library Instruction</p></div>
    </div>
    <div class="track" style="left:69px;top:722px">
      <div class="track-shadow"></div><div class="track-tab"></div><div class="track-card"></div>
      <div class="track-ring">5</div>
      <div class="track-text"><h2 class="track-name">Swimming Together</h2><p class="track-desc">Collaborating with<br>Others</p></div>
    </div>
    <div class="track" style="left:455px;top:722px">
      <div class="track-shadow"></div><div class="track-tab"></div><div class="track-card"></div>
      <div class="track-ring">6</div>
      <div class="track-text"><h2 class="track-name">The Bermuda Triangle</h2><p class="track-desc">Exploring (Seemingly)<br>Eternal Challenges</p></div>
    </div>
  </section>

  <svg class="footer-band" viewBox="0 0 891 340" aria-hidden="true">
    <path d="M0 124 Q445 -22 891 124 L891 340 L0 340 Z" fill="var(--light-teal)"/>
    <path d="M0 132 Q445 -12 891 132 L891 340 L0 340 Z" fill="var(--teal)"/>
    <path d="M0 138 Q445 -4 891 138 L891 340 L0 340 Z" fill="var(--band-blue)"/>
  </svg>

  <div class="books" role="img" aria-label="Photo of a row of standing hardcover books"></div>

  <footer class="footer-text">
    <p class="footer-title">Conference Starting</p>
    <p class="footer-meta">MAY 7-9 &nbsp;/ TRIVAN Cedar Bay, VA</p>
  </footer>

  <div class="web-pill">
    <svg class="web-icon" viewBox="0 0 20 20" fill="none" stroke="#ffffff" stroke-width="1.4" aria-hidden="true">
      <circle cx="10" cy="10" r="8"/>
      <ellipse cx="10" cy="10" rx="3.5" ry="8"/>
      <line x1="2" y1="10" x2="18" y2="10"/>
      <line x1="3.5" y1="6" x2="16.5" y2="6"/>
      <line x1="3.5" y1="14" x2="16.5" y2="14"/>
    </svg>
    <span>www.trivancedarbay.com</span>
  </div>
</main>
</body>
</html>
```